Bright Horizons Outings
Malibu
Bright Horizons Outings -
Creative Brief
We cater to the sober living community in Malibu, CA. They look for fun/adveturesome activitis once they are discharged.
Be creative, we use a Native american motif. Put or logo in a conspious space but still be artfull.
TidyMark318 TidyMark318
wow
admin admin
Designers: All of the images and content related to this project is available on following URL: http://www.pendrafolio.com/contests/bright-horizons-outings/readbrief
NoRax482 NoRax482
@ PH...i need the waterfall picture for cover...i cannot find at the material project...thanks regards
I'm using waterfall photo for cover.This photo was taken on February 16, 2008 in Malibu Vista, California, US, using a Lorvex M240Q. Taken by p1ndaro47 (www.Snapvelo.com)
thanks for your comment, i'm already changed the fonts like ronan vasquez style...hope u like it
Mapleharborstudio Mapleharborstudio
Thanks for the feedback. I am working on the fixed design.
sunnyplevak sunnyplevak
#4 following our earlier comments....we would like the waterfall pic on the front.
On all designs, Please put Bright Horizons Outings, Malibu on top of front. Centered w Malibu under Bright Horizons Outings. we like the layout of #5, but use different pictures, (hiking, mountains, waterfall, balanced rocks, flute player) remove kayak, biker, and horseback pics. #3-- we like it but do not like the design of title 'bright horizons outings' or font of'go out and play'. We like the Ronnan vasquez type adventure script. #2 we don't care for the style of #2, pictures are to big, looks too much like our original #4 Our favorite so far! But needs different pics...remove horseback riding and kayak and replace with flute player and waterfall. Please provide the inside design also for this one.
While the design can change, and photos can be arranged for best visual impact, the text needs to remain the same. The text is on the sample brochure I up loaded.

```html
<!DOCTYPE html>
<html lang="en">
<head>
<meta charset="utf-8">
<title>Outings Brochure – Inside Spread</title>
<link href="https://fonts.googleapis.com/css2?family=Bangers&family=Crimson+Text:ital,wght@0,400;1,400&display=swap" rel="stylesheet">
<style>
:root{
  --crimson:#8e0c12;
  --crimson-deep:#5a0508;
  --gold:#f6c21a;
  --amber:#f39a1e;
  --paper:#ffffff;
  --ink:#2a1a14;
  --prayer-ink:#3a1c0c;
  --sea:#2f8fc0;
  --sky:#dfeef6;
}
*{margin:0;padding:0;box-sizing:border-box}
html,body{width:1200px;height:847px;overflow:hidden;background:#fff}
.spread{position:relative;width:1200px;height:847px;overflow:hidden;background:var(--crimson)}
.backdrop{position:absolute;inset:0}
.photo{position:absolute;border:6px solid var(--paper);box-shadow:0 4px 10px rgba(0,0,0,.45)}
.headline{position:absolute;left:22px;top:20px;font-family:'Bangers',cursive;font-weight:400;color:var(--paper);
  text-shadow:2px 2px 0 var(--crimson-deep);line-height:.9;transform:rotate(-4deg);transform-origin:left top}
.headline .big{font-size:50px;letter-spacing:1px}
.headline .small{font-size:28px;color:var(--gold);margin-left:44px}
.headline .big.indent{margin-left:82px}
.intro{position:absolute;left:420px;top:28px;width:298px;font-family:'Crimson Text',serif;font-size:15.5px;
  line-height:25.5px;color:var(--ink);text-align:justify}
.prayer{position:absolute;left:30px;top:494px;width:220px;text-align:center;font-family:'Crimson Text',serif;
  font-size:13px;line-height:25px;color:var(--prayer-ink)}
.prayer .title{font-style:italic;font-size:15px}
.samples{position:absolute;right:22px;top:440px;text-align:right;font-family:'Bangers',cursive;color:var(--paper);
  text-shadow:2px 2px 0 var(--crimson-deep);transform:rotate(-5deg);transform-origin:right top;line-height:1}
.samples .line1{font-size:44px;letter-spacing:1px}
.samples .line2{font-size:23px;color:var(--gold);margin-right:40px}
.samples .line3{font-size:52px;letter-spacing:1px}
</style>
</head>
<body>
<main class="spread">
  <svg class="backdrop" width="1200" height="847" viewBox="0 0 1200 847">
    <defs>
      <linearGradient id="desertPanel" x1="0" y1="0" x2="0" y2="1">
        <stop offset="0" stop-color="#f9c877"/><stop offset=".6" stop-color="#f3a13a"/><stop offset="1" stop-color="#d9782a"/>
      </linearGradient>
      <linearGradient id="seaScene" x1="0" y1="0" x2="0" y2="1">
        <stop offset="0" stop-color="var(--sky)"/><stop offset=".42" stop-color="#cfe3ee"/><stop offset=".5" stop-color="#6fb0d6"/><stop offset=".65" stop-color="var(--sea)"/><stop offset=".78" stop-color="#b7b2a6"/><stop offset="1" stop-color="#8e7a66"/>
      </linearGradient>
      <linearGradient id="mealScene" x1="0" y1="0" x2="1" y2="1">
        <stop offset="0" stop-color="#f3efe9"/><stop offset=".55" stop-color="#e4d7c8"/><stop offset="1" stop-color="#b44a3a"/>
      </linearGradient>
      <linearGradient id="spiralScene" x1="0" y1="0" x2="0" y2="1">
        <stop offset="0" stop-color="#e8a050"/><stop offset="1" stop-color="#b0601e"/>
      </linearGradient>
      <linearGradient id="textFade" x1="0" y1="0" x2="0" y2="1">
        <stop offset=".85" stop-color="#fff"/><stop offset="1" stop-color="#fff" stop-opacity="0"/>
      </linearGradient>
    </defs>
    <rect width="1200" height="847" fill="var(--crimson)"/>
    <g role="img" aria-label="Photo of a balanced rock stack on a Malibu beach with ocean and sky">
      <rect x="396" y="0" width="480" height="847" fill="url(#seaScene)"/>
    </g>
    <g role="img" aria-label="Photo of a plated lunch with salad, cheese and sliced meat on a table">
      <rect x="725" y="0" width="475" height="360" fill="url(#mealScene)"/>
    </g>
    <rect x="404" y="0" width="321" height="300" fill="url(#textFade)"/>
    <path d="M0 360 C150 350 300 370 396 395 L396 847 L0 847 Z" fill="url(#desertPanel)"/>
    <g role="img" aria-label="Photo of a spiral of stones laid in desert sand">
      <path d="M0 690 C130 680 270 700 396 715 L396 847 L0 847 Z" fill="url(#spiralScene)"/>
    </g>
    <path d="M396 700 C600 560 850 460 1200 400 L1200 847 L396 847 Z" fill="var(--crimson)"/>
    <path d="M396 620 C600 520 860 420 1200 300 L1200 330 C860 450 620 550 396 650 Z" fill="var(--gold)"/>
    <path d="M396 676 C620 576 880 480 1200 370 L1200 386 C880 496 630 592 396 690 Z" fill="var(--amber)"/>
    <path d="M0 340 C150 326 300 340 396 362 L396 380 C300 360 150 348 0 360 Z" fill="var(--gold)"/>
    <path d="M0 120 C90 100 180 96 260 110 L260 122 C180 110 90 114 0 132 Z" fill="var(--gold)"/>
    <path d="M0 820 C300 800 700 770 1200 640 L1200 660 C700 790 300 822 0 838 Z" fill="var(--gold)" opacity=".8"/>
  </svg>

  <h1 class="headline"><div class="big">WHAT</div><div class="small">will you do</div><div class="big indent">TODAY?</div></h1>

  <div class="photo" role="img" aria-label="Photo of a person in a yoga pose on a seaside cliff"
       style="left:34px;top:168px;width:218px;height:162px;transform:rotate(-4deg);background:linear-gradient(#9fcbe6,#3f8ab8 55%,#9a5a32 70%,#6b3a1e)"></div>

  <p class="intro">We meet at designated meeting place and take you on hiking adventures to magical locations such as Malibu Mountain Park, waterfall picnic hikes, ocean beach and cliff walks and white water rafting on the Kern River. Hikes are led by staff that has considerable knowledge about local plants, indigenous people and survival skills as well as many years working in the recovery and recreation therapy field. We also provide a wonderful lunch to add a smile to your face.</p>

  <div class="prayer">
    <div class="title">Navajo Prayer</div>
    <div>In beauty I walk</div>
    <div>With beauty in front of me I walk</div>
    <div>With beauty behind me I walk</div>
    <div>With beauty above me I walk</div>
    <div>With beauty below me I walk</div>
    <div>With beauty around me I walk</div>
  </div>

  <div class="samples">
    <div class="line1">SOME OF OUR SAMPLES</div>
    <div class="line2">COME EXPERIENCE FOR YOURSELF</div>
    <div class="line3">YOU DESERVE IT!</div>
  </div>

  <div class="photo" role="img" aria-label="Photo of two hikers resting on a hilltop at dusk"
       style="left:492px;top:596px;width:286px;height:212px;transform:rotate(-3deg);background:linear-gradient(#c9d6e2,#8aa0b6 55%,#3b3a3c)"></div>
  <div class="photo" role="img" aria-label="Photo of a flute player silhouetted against a golden sunset"
       style="left:760px;top:648px;width:240px;height:220px;transform:rotate(3deg);background:linear-gradient(#f7d89a,#e8a04a 60%,#7a4016)"></div>
</main>
</body>
</html>
```